Modern Banner and Window Decal Design For Law Firm Lawyer

We are looking for three modern and sophisticated banner design and window decal for our law firm.

Banner measurements/types:

1) Height: 130 cm Width: 160 cm (Outdoor banner)
2) Height: 200 cm Width: 85 cm (Pull up/retractable indoor banner)

Window Decal:
3) Height: 70cm width 70cm

Our law firm is based in Melbourne, Australia and we deal with property law mostly.

We prefer a white background with classic text in black or grey. We would also like a dash of colour so please use a green, blue or aqua colour palette that is consistent with our logo. Vector attached. A nice photo of property, Melbourne city viee, or family home would be nice.

We do not want any law related images - scales of justice, gavel or the like.

Our ultimate goal is to communicate that the firm is modern, professional and knowledgeable

We would like the following:

1. Our logo
2. Our services: - Property Law - Wills - Powers of Attorney - Probate - Estate Administration - Consultancy & Agency
3. Phone number
4. Web Address

5. For pull up/retractable banner we would also like the following text:

We use the latest digital technology and fixed-fees to provide fast and affordable legal advice that is easy to understand.

For privacy reasons, we will provide business details once we have decided on the winner.

We will monitor entries closely and promise to provide feedback and guidance on each entry.

Thank you very much for considering this project.

Target Market(s)

General public, professionals, lawyers and conveyancers

Industry/Entity Type

Law Firm

Font styles to use
Sans Serif

Colors
0393ce
34a6d7
0456a4
3176b5
acd037
33b8a4
86cfc6
00a990
9ccb3b

Requirements
Must have
• 1. Our logo
• 2. Our services: - Property Law - Wills - Powers of Attorney - Probate & Estate Administration - Consultancy & Agency
• 3. Phone number
• 4. Web Address
Nice to have
• Picture of Melbourne, Australia city ; property/buildings/lawyers
Should not have
• We do not want any law related images - scales of justice, gavel or the like.

```html
<!DOCTYPE html>
<html lang="en">
<head>
<meta charset="utf-8">
<title>Ridgeview Lawyers – Banners</title>
<link rel="stylesheet" href="https://fonts.googleapis.com/css2?family=Montserrat:wght@400;500;600&display=swap">
<style>
  :root {
    --stage: #e6e9ed;
    --paper: #ffffff;
    --ink: #4a4a4c;
    --accent: #2e9fd6;
    --glass-light: #dfe8f1;
    --glass-mid: #8fb0cf;
    --glass-deep: #3f6d9c;
  }
  * { box-sizing: border-box; margin: 0; padding: 0; }
  html, body { width: 1200px; height: 1200px; overflow: hidden; }
  body {
    background: var(--stage);
    font-family: "Montserrat", sans-serif;
    color: var(--ink);
    position: relative;
  }
  .banner {
    position: absolute;
    background: var(--paper);
    display: flex;
    flex-direction: column;
    align-items: center;
    overflow: hidden;
    box-shadow: 0 6px 24px rgba(0,0,0,.12);
  }
  .brand {
    display: flex;
    align-items: center;
    gap: 14px;
    color: var(--ink);
    font-weight: 500;
  }
  .brand-dot {
    border-radius: 50%;
    background: var(--accent);
    flex: none;
  }
  .brand-name { display: flex; flex-direction: column; line-height: 1.1; }
  .brand-name .primary { letter-spacing: .02em; }
  .brand-name .secondary { letter-spacing: .12em; }
  .services {
    text-align: center;
    font-weight: 500;
    text-transform: uppercase;
    color: var(--ink);
  }
  .sep {
    display: inline-block;
    width: 9px; height: 9px;
    border-radius: 50%;
    background: var(--accent);
    vertical-align: middle;
  }
  .contact { color: var(--accent); font-weight: 600; }
  .city-photo {
    width: 100%;
    margin-top: auto;
    background: linear-gradient(to bottom, var(--paper) 0%, var(--glass-light) 20%, var(--glass-mid) 55%, var(--glass-deep) 100%);
  }

  /* Outdoor banner 160 × 130 */
  .banner--outdoor { left: 40px; top: 310px; width: 720px; height: 585px; padding-top: 30px; }
  .banner--outdoor .brand-dot { width: 96px; height: 96px; }
  .banner--outdoor .primary { font-size: 32px; }
  .banner--outdoor .secondary { font-size: 19px; }
  .banner--outdoor .services { margin-top: 28px; font-size: 24px; line-height: 1.95; }
  .banner--outdoor .services .sep { margin: 0 14px; }
  .banner--outdoor .contact { margin-top: 6px; font-size: 25px; display: flex; gap: 44px; }
  .banner--outdoor .city-photo { height: 180px; }

  /* Pull-up banner 85 × 200 */
  .banner--pullup { left: 810px; top: 170px; width: 350px; height: 860px; padding-top: 26px; }
  .banner--pullup .brand-dot { width: 100px; height: 100px; }
  .banner--pullup .primary { font-size: 27px; }
  .banner--pullup .secondary { font-size: 17px; }
  .banner--pullup .services { margin-top: 36px; font-size: 20px; line-height: 1.4; }
  .banner--pullup .services li { list-style: none; }
  .banner--pullup .services .sep { display: block; margin: 4px auto; width: 7px; height: 7px; }
  .banner--pullup .contact { margin-top: 26px; font-size: 22px; text-align: center; line-height: 1.65; }
  .banner--pullup .contact .phone { font-size: 25px; }
  .banner--pullup .intro { margin-top: 26px; padding: 0 16px; font-size: 15px; line-height: 1.45; align-self: stretch; }
  .banner--pullup .city-photo { height: 200px; }
</style>
</head>
<body>

  <section class="banner banner--outdoor" aria-label="Outdoor banner">
    <div class="brand">
      <span class="brand-dot"></span>
      <div class="brand-name">
        <span class="primary">RIDGEVIEW</span>
        <span class="secondary">LAWYERS</span>
      </div>
    </div>
    <p class="services">
      Powers of Attorney<span class="sep"></span>Property Law<br>
      Wills<span class="sep"></span>Consultancy &amp; Agency<br>
      Estate Administration<span class="sep"></span>Probate
    </p>
    <p class="contact"><span>ridgeviewlawyers.com.au</span><span>01 9876 5432</span></p>
    <div class="city-photo" role="img" aria-label="Photo of glass office towers seen from below, fading into a hazy sky"></div>
  </section>

  <section class="banner banner--pullup" aria-label="Pull-up banner">
    <div class="brand">
      <span class="brand-dot"></span>
      <div class="brand-name">
        <span class="primary">RIDGEVIEW</span>
        <span class="secondary">LAWYERS</span>
      </div>
    </div>
    <ul class="services">
      <li>Powers of Attorney</li><li><span class="sep"></span></li>
      <li>Property Law</li><li><span class="sep"></span></li>
      <li>Wills</li><li><span class="sep"></span></li>
      <li>Consultancy &amp; Agency</li><li><span class="sep"></span></li>
      <li>Estate Administration</li><li><span class="sep"></span></li>
      <li>Probate</li>
    </ul>
    <p class="contact">ridgeviewlawyers.com.au<br><span class="phone">01 9876 5432</span></p>
    <p class="intro">We use the latest digital technology and fixed-fees to provide fast and affordable legal advice that is easy to understand.</p>
    <div class="city-photo" role="img" aria-label="Photo of a glass skyscraper rising into a misty sky"></div>
  </section>

</body>
</html>
```